Landing page and nested content pages for HillsideFaithful.com

Web design for existing site https://hillsidefaithful.example/

This is a RESPONSIVE web site that needs to work on a medium-res mobile device and also look great on a widescreen desktop.

There are three or four public pages we currently have that need a fresh design, which will be used somewhat to guide the design direction for the non-public interior site for logged-in users in a later design effort.

The recently created new logo is attached and the new design should be based on this logo, I don't know how you'll do it, but the new logo should fit appropriately; the current web site's little logo on the top left must be thrown out, and one of our goals in this design effort is to set up the top nav bar, logo placement, etc. There are multiple logos attached to this project but the primary one to try for is the red door one. The other logos (gray+red arc logo and tree logo) are there in case you as the designer prefer them and can demonstrate that they are more suited for a web design than the red one. Otherwise I am hoping to see the red logo used for the site overall and the other logos to highlight discipleship and/or fellowship sections on the site.

The main pages are: 1) landing page, which describes the function of the site for logged-in users (not actually a part of this design project but the logged-in users' site redesign should be inspired by this effort) with multiple bits of content embedded on the page, and 2) a content page called "The Essentials" which contains several pages worth of content. The content is currently just a wall of text; it needs to be somehow broken down into clickable sections and imagery applied to make it interesting. 3) We also have some more minor pages which I'll list below.

The Landing Page

This is to redesign the content at https://hillsidefaithful.example/
The current web site's placeholder content represents the general direction desired for the landing page, but I'm not a designer, so colors and layout etc can be totally re-thought. I'd like to use these images and these highlights. I've uploaded the stock images.

The web site on the whole for logged-in users (again, not itself a part of this design) is part social network and part library of various guides and resources. So the landing page needs to highlight the objectives of the site while demonstrating some of the features of the site. There is currently also some additional text content that should also be there, but should not be so prominently displayed as it is today; it should be accessible from some scrolling and/or from a button-click pop-over, so that new visitors are not inundated with a wall of text. Besides the logo, I've uploaded some features of the site that might be useful in graphically highlighting the features of the site.

'The Essentials' Content Page

This is to redesign the content at https://hillsidefaithful.example/Gospel

The content at this URL is currently one big wall of text, and it is intimidating enough that people may not be likely to read it. It needs to be read.

Other minor content pages

We also have these pages that needs to demonstrate a "theme" of basic content pages' design strategy for basic content:

https://hillsidefaithful.example/freebibleresponse
and
https://hillsidefaithful.example/bibledistribution

We will be adding additional content pages later, but we need to finalize the design theme before proceeding.

As currently demonstrated, I tend to prefer a serif font for headings (for theming around ancient-yet-current faith-based content), sans-serif for paragraphs (for readability), which is why the current site uses the fonts it has. Find some better fonts as you please.

The images prefixed with "interior-features-" are for landing page reference only, you might choose to highlight a cropped snippet, but don't go too crazy since these features will themselves be redesigned and so we will need to replace whatever cropped sample you might use with another one later.

There will be login and register functions. I DO NOT want any of this functionality to be built, but I do want the core public-site UX concept built out with *CLEAN* and attractive markup in HTML+CSS(+JS?) based on Bootstrap 4.

Target Market(s)

Christians looking for fellowship and discipleship outside of traditional church buildings (in-home fellowship, online fellowship, online study resources)

• Landing page entices the user to register
'Essentials' page somehow redistributes content into meaningful sections
Other minor content pages are redesigned but not too complicated, so that future content pages can follow suit
Designer can choose the logo out of 3, but the red door logo was the preferred logo if you can work with it and integrate it into the site such as with a responsive site top nav bar logo
HTML+CSS must be clean and based on Bootstrap 4

```html
<!DOCTYPE html>
<html lang="en">
<head>
<meta charset="utf-8">
<title>Hillside Faithful</title>
<link rel="stylesheet" href="https://fonts.googleapis.com/css2?family=Cinzel:wght@400;700&family=Open+Sans:wght@400;600&display=swap">
<style>
:root{
  --red:#9b0d14;
  --ink:#2a2a2a;
  --muted:#6f6f6f;
  --dark:#262626;
  --white:#ffffff;
  --icon-tint:#f3e7e7;
}
*{margin:0;padding:0;box-sizing:border-box}
html,body{width:1200px;height:4431px;overflow:hidden;background:var(--white)}
body{position:relative;font-family:"Open Sans",Arial,sans-serif;color:var(--ink)}
.abs{position:absolute}
.serif{font-family:"Cinzel",Georgia,serif;font-weight:400}
.red{color:var(--red)}

/* hero */
.hero{position:absolute;left:0;top:0;width:1200px;height:800px;overflow:hidden}
.hero-photo{position:absolute;inset:0;background:linear-gradient(120deg,#6b5444 0%,#3c3431 35%,#5d6b85 62%,#8a7a6c 85%,#b9a898 100%)}
.hero-shade{position:absolute;inset:0;background:linear-gradient(90deg,rgba(0,0,0,.35),rgba(0,0,0,.05))}
.hero-curve{position:absolute;left:0;top:0}
.brand{position:absolute;color:var(--white);font-family:"Open Sans",Arial,sans-serif;font-weight:600;letter-spacing:1px;text-transform:uppercase;text-align:center;line-height:1.1}
.brand-top{left:110px;top:60px;width:200px;font-size:30px}
.nav-toggle{left:814px;top:36px;width:22px;height:18px}
.nav-toggle span{display:block;height:3px;background:var(--white);margin-bottom:4px}
.btn-login{left:854px;top:24px;width:102px;height:48px;border:2px solid #eee;border-radius:4px;color:var(--white);font-size:17px;display:flex;align-items:center;justify-content:center;gap:6px}
.btn-register{left:964px;top:24px;width:124px;height:48px;background:var(--red);border-radius:4px;color:var(--white);font-size:17px;display:flex;align-items:center;justify-content:center;gap:6px}
.hero-title{left:110px;top:225px;color:var(--white);font-size:76px;line-height:90px}
.slider-dots{left:568px;top:540px;display:flex;gap:5px}
.slider-dots span{width:13px;height:13px;border:2px solid var(--white);border-radius:50%}
.slider-dots span.on{background:var(--white)}

/* welcome */
.welcome-title{left:0;top:742px;width:1200px;text-align:center;font-size:45px}
.welcome-text{left:210px;top:814px;width:780px;text-align:center;font-size:16px;line-height:26px;color:var(--muted)}
.welcome-sub{left:0;top:892px;width:1200px;text-align:center;font-size:20px;font-weight:600;color:var(--ink)}
.purpose{top:952px;width:240px;text-align:center}
.purpose-icon{width:120px;height:120px;margin:0 auto 18px;border-radius:16px;background:linear-gradient(135deg,var(--icon-tint),#ece8e8)}
.purpose p{font-size:16px;line-height:24px;color:var(--muted)}

/* bible band */
.bible{left:0;top:1258px;width:1200px;height:380px}
.bible-photo{position:absolute;inset:0;background:linear-gradient(90deg,#e4e2df,#cfcac4 40%,#dedbd7 70%,#c9c5bf)}
.bible-veil{position:absolute;inset:0;background:rgba(255,255,255,.55)}
.bible-title{left:0;top:82px;width:1200px;text-align:center;font-size:45px}
.bible-text{left:160px;top:152px;width:880px;text-align:center;font-size:16px;line-height:26px;color:#555}
.btn-essential{left:504px;top:234px;width:192px;height:62px;background:var(--red);border-radius:4px;color:var(--white);font-size:17px;font-weight:600;display:flex;align-items:center;justify-content:center}

/* features */
.feature-photo{width:500px;height:375px;border-radius:0 0 34px 0}
.feature-title{font-size:45px;line-height:52px}
.feature-text{font-size:16px;line-height:26px;color:var(--muted);margin-top:22px}

/* footer */
.footer{left:0;top:3740px;width:1200px;height:691px;background:var(--dark)}
.footer-curve{position:absolute;left:0;top:0}
.contact-title{left:0;top:220px;width:1200px;text-align:center;color:var(--white);font-size:45px}
.contact-text{left:0;top:282px;width:1200px;text-align:center;color:#e8e8e8;font-size:16px}
.contact-mail{left:0;top:312px;width:1200px;text-align:center;color:var(--white);font-size:21px;display:flex;justify-content:center;align-items:center;gap:10px}
.footer-rule{left:146px;top:358px;width:908px;height:1px;background:#555}
.brand-foot{left:0;top:470px;width:1200px;font-size:36px}
.copyright{left:0;top:570px;width:1200px;text-align:center;color:#e0e0e0;font-size:16px}
.social{left:516px;top:602px;display:flex;gap:14px}
.social span{width:48px;height:48px;border:2px solid var(--white);border-radius:50%}
</style>
</head>
<body>

<header class="hero">
  <div class="hero-photo" role="img" aria-label="Hands folded in prayer over an open Bible on a wooden table"></div>
  <div class="hero-shade"></div>
  <svg class="hero-curve" width="1200" height="800" viewBox="0 0 1200 800">
    <path d="M0,790 Q520,560 1200,676 L1200,800 L0,800 Z" fill="#ffffff"/>
    <path d="M172,726 Q560,565 1135,668 Q560,610 172,726 Z" fill="#9b0d14"/>
  </svg>
  <div class="brand brand-top">Hillside Faithful</div>
  <div class="abs nav-toggle"><span></span><span></span><span></span></div>
  <div class="abs btn-login">
    <svg width="13" height="15" viewBox="0 0 13 15"><rect x="1" y="6" width="11" height="9" rx="1" fill="#fff"/><path d="M3.5,6 V4 a3,3 0 0 1 6,0 V6" fill="none" stroke="#fff" stroke-width="2"/></svg>
    LOGIN
  </div>
  <div class="abs btn-register">
    <svg width="14" height="14" viewBox="0 0 14 14"><path d="M2,12 L3,9 L10,2 L12,4 L5,11 Z" fill="#fff"/></svg>
    REGISTER
  </div>
  <h1 class="abs serif hero-title">CHRISTIAN,<br>MEET CHRISTIAN</h1>
  <div class="abs slider-dots"><span class="on"></span><span></span><span></span><span></span></div>
</header>

<section>
  <h2 class="abs serif welcome-title">WELCOME TO <span class="red">HILLSIDE FAITHFUL</span></h2>
  <p class="abs welcome-text">We intends to encourage Christian neighbors to discover and support one another as a network of believers, including in fellowship, in discipleship, and in practical support.</p>
  <p class="abs welcome-sub">God desires you and all of us to:</p>

  <div class="abs purpose" style="left:109px">
    <div class="purpose-icon" role="img" aria-label="Icon of three connected people"></div>
    <p>Find institutional churches, where believers can assemble, sing to God together, and glean from prepared messages</p>
  </div>
  <div class="abs purpose" style="left:355px">
    <div class="purpose-icon" role="img" aria-label="Icon of a house church"></div>
    <p>Discover house churches, where love and true participation with the Body of Christ can reign</p>
  </div>
  <div class="abs purpose" style="left:602px">
    <div class="purpose-icon" role="img" aria-label="Icon of hands supporting a group"></div>
    <p>Find other believers as they willfully make themselves vulnerable to other believers, so that we can all support one another.</p>
  </div>
  <div class="abs purpose" style="left:855px">
    <div class="purpose-icon" role="img" aria-label="Icon of an online profile board"></div>
    <p>Interact with one another online and share discipleship - producing content, using basic social network features</p>
  </div>
</section>

<section class="abs bible">
  <div class="bible-photo" role="img" aria-label="Soft background of a group studying the Bible together"></div>
  <div class="bible-veil"></div>
  <h2 class="abs serif bible-title">HOW AND WHY <span class="red">TO READ THE BIBLE</span></h2>
  <p class="abs bible-text">We use the Bible as the basis for discussing Jesus and Christianity. The Bible is a compilation of 66 books—scrolls, originally—that were penned by humans, but we believe were completely inspired by the Holy Spirit.</p>
  <div class="abs btn-essential">VIEW ESSENTIAL</div>
</section>

<section>
  <div class="abs feature-photo" style="left:112px;top:1719px;background:linear-gradient(135deg,#8c7a5e,#b8a27a 45%,#7f8a4e)" role="img" aria-label="Two neighbours talking over a garden fence"></div>
  <div class="abs" style="left:688px;top:1785px;width:440px">
    <h3 class="serif feature-title">FIND NEARBY<br><span class="red">BELIEVERS</span></h3>
    <p class="feature-text">Form fellowships, bible studies, home churches, and participate in activities with church establishments.</p>
  </div>

  <div class="abs" style="left:108px;top:2233px;width:440px">
    <h3 class="serif feature-title">SHARE YOUR<br><span class="red">HEART AND MIND</span></h3>
    <p class="feature-text">Post your thoughts or publish articles pertaining to the faith, receive feedback from other believers.</p>
  </div>
  <div class="abs feature-photo" style="left:586px;top:2133px;background:linear-gradient(135deg,#c9a77a,#e8c99a 40%,#9c8a6a 75%,#5e5646)" role="img" aria-label="Girl holding a Bible in a field at sunset"></div>

  <div class="abs feature-photo" style="left:112px;top:2556px;background:linear-gradient(135deg,#d9d4cc,#9aa4b4 45%,#2a5fb0 85%)" role="img" aria-label="Group sitting in a circle holding hands in prayer"></div>
  <div class="abs" style="left:688px;top:2620px;width:440px">
    <h3 class="serif feature-title">MEET, GROW, AND<br><span class="red">PRAY TOGETHER</span></h3>
    <p class="feature-text">Meet together, online or in person. Praise and worship Jesus together. Teach one another. Admonish and exhort. Pray for one another in love.</p>
  </div>

  <div class="abs" style="left:108px;top:3053px;width:440px">
    <h3 class="serif feature-title">SCHEDULE<br><span class="red">OUTREACHES</span></h3>
    <p class="feature-text">Commit to reaching out to the community, bringing food, clothing, or just lots of God's love.</p>
  </div>
  <div class="abs feature-photo" style="left:586px;top:2969px;background:linear-gradient(135deg,#c7a881,#d9c3a3 45%,#4f9ea3 80%,#2c6e78)" role="img" aria-label="Volunteers packing canned food into donation boxes"></div>

  <div class="abs feature-photo" style="left:112px;top:3390px;background:linear-gradient(135deg,#5d7a3e,#8aa25a 40%,#b3805a 70%,#6b4a3a)" role="img" aria-label="Missionary surrounded by smiling village children"></div>
  <div class="abs" style="left:688px;top:3433px;width:480px">
    <h3 class="serif feature-title">GO GLOBAL, TO<br><span class="red">EVERY TRIBE, EVERY TONGUE, EVERY NATION</span></h3>
    <p class="feature-text">Find and support organizations that are reaching around the world to share the love of Jesus, or go yourself.</p>
  </div>
</section>

<footer class="abs footer">
  <svg class="footer-curve" width="1200" height="180" viewBox="0 0 1200 180">
    <path d="M0,0 L1200,0 L1200,12 Q700,150 0,86 Z" fill="#ffffff"/>
    <path d="M66,80 Q520,178 1030,72 Q520,140 66,80 Z" fill="#9b0d14"/>
  </svg>
  <h2 class="abs serif contact-title">CONTACT <span class="red">US</span></h2>
  <p class="abs contact-text">We just got this place, come back in a bit. If you want to reach out, send an e-mail to</p>
  <p class="abs contact-mail">
    <svg width="20" height="15" viewBox="0 0 20 15"><rect x="0" y="0" width="20" height="15" rx="2" fill="#fff"/><path d="M1,1.5 L10,8 L19,1.5" fill="none" stroke="#262626" stroke-width="1.6"/></svg>
    jon@hillsidefaithful.example
  </p>
  <div class="abs footer-rule"></div>
  <div class="brand brand-foot">Hillside Faithful</div>
  <p class="abs copyright">© 2021 - Hillside Faithful. All rights reserved.</p>
  <div class="abs social"><span></span><span></span><span></span></div>
</footer>

</body>
</html>
```